I need a business card design for my new clinic (ATHLETIC CARE OF JOINT). I am orthopedist, expert in sports surgery, especially knee surgery. I prefer, as colors, the colors of my logo (green, black and white). I already have my logo and should appear on my card. It's good to see my site to have ideas (www.drlucianovarela.example)
It needs contain:
my name: Dr. Luciano Varela
my registration: CRM 584-902
my specialty: Cirurgia do Joelho / Esporte
my address: Centro Empresarial - Parque Aurora Mall
Av. Doutor Augusto Valadares Pinto, 2740 sala 803
Jd. Acácias - Ribeirão Preto - SP
my phone number: Tel (16) 8420-5937
my clinic phone: (16) 3745-8081
my e-mail: drlucianovarela@mailbox.example
my site: www.drlucianovarela.example

Target Market(s)

futures patients

Industry/Entity Type

Clinic

Requirements
Nice to have
• letters not overfilled
straight lines, with few curves

```html
<!DOCTYPE html>
<html lang="pt-BR">
<head>
<meta charset="utf-8">
<title>Varela – Cartão de Visita</title>
<link rel="stylesheet" href="https://fonts.googleapis.com/css2?family=Cabin:wght@400;500;600&display=swap">
<style>
  :root {
    --green: #3fb878;
    --green-dark: #2f9c60;
    --black: #1b1a1d;
    --white: #ffffff;
    --grey-text: #d4d4d4;
    --page: #e9e9e9;
  }
  html, body {
    margin: 0;
    padding: 0;
    width: 1200px;
    height: 900px;
    overflow: hidden;
    background: var(--page);
    font-family: "Cabin", sans-serif;
  }
  .stage {
    position: relative;
    width: 1200px;
    height: 900px;
  }
  .card {
    position: absolute;
    left: 240px;
    width: 720px;
    height: 400px;
    border-radius: 22px;
    overflow: hidden;
    box-shadow: 0 4px 14px rgba(0,0,0,0.18);
  }
  /* Back side */
  .card-back {
    top: 30px;
    background: var(--green);
  }
  .card-back .brand-name {
    position: absolute;
    left: 360px;
    top: 130px;
    margin: 0;
    font-size: 64px;
    font-weight: 500;
    letter-spacing: 2px;
    color: var(--black);
  }
  .card-back .site {
    position: absolute;
    left: 372px;
    top: 230px;
    margin: 0;
    font-size: 17px;
    color: var(--white);
  }
  /* Front side */
  .card-front {
    top: 470px;
    background: var(--white);
  }
  .card-front .shapes {
    position: absolute;
    inset: 0;
  }
  .registration {
    position: absolute;
    left: 32px;
    top: 58px;
    margin: 0;
    font-size: 12px;
    font-weight: 600;
    color: var(--black);
  }
  .brand {
    position: absolute;
    right: 40px;
    top: 26px;
    display: flex;
    align-items: center;
    gap: 14px;
  }
  .brand-square {
    width: 52px;
    height: 52px;
    background: var(--green);
    border-radius: 6px;
  }
  .brand .brand-name {
    margin: 0;
    font-size: 44px;
    font-weight: 500;
    letter-spacing: 1px;
    color: var(--black);
  }
  .doctor {
    position: absolute;
    left: 40px;
    top: 172px;
  }
  .doctor-name {
    margin: 0;
    font-size: 26px;
    font-weight: 500;
    color: var(--green);
  }
  .specialty {
    margin: 2px 0 0;
    font-size: 18px;
    color: var(--black);
  }
  .address {
    position: absolute;
    right: 34px;
    top: 228px;
    margin: 0;
    text-align: right;
    font-style: normal;
    font-size: 14px;
    line-height: 23px;
    color: var(--grey-text);
  }
  .contacts {
    position: absolute;
    left: 40px;
    top: 318px;
    margin: 0;
    padding: 0;
    list-style: none;
    font-size: 17px;
    line-height: 24px;
    color: var(--white);
  }
  .contacts .label {
    display: inline-block;
    width: 18px;
    color: var(--green);
    font-size: 14px;
  }
</style>
</head>
<body>
<main class="stage">

  <section class="card card-back" aria-label="Verso do cartão">
    <h2 class="brand-name">VARELA</h2>
    <p class="site">www.drlucianovarela.example</p>
  </section>

  <section class="card card-front" aria-label="Frente do cartão">
    <svg class="shapes" viewBox="0 0 720 400" width="720" height="400" aria-hidden="true">
      <path d="M0,252 C150,244 340,216 520,172 C350,226 160,258 0,266 Z" fill="var(--black)"/>
      <path d="M0,272 C220,256 500,176 720,78 L720,104 C500,204 210,282 0,298 Z" fill="var(--green)"/>
      <path d="M0,298 C210,282 500,204 720,104 L720,400 L0,400 Z" fill="var(--black)"/>
    </svg>

    <p class="registration">CRM 584-902</p>

    <div class="brand">
      <span class="brand-square"></span>
      <h2 class="brand-name">VARELA</h2>
    </div>

    <div class="doctor">
      <h1 class="doctor-name">Dr. Luciano Varela</h1>
      <p class="specialty">Cirurgia do Joelho / Esporte</p>
    </div>

    <address class="address">
      Centro Empresarial - Parque Aurora Mall<br>
      Av. Doutor Augusto Valadares Pinto, 2740<br>
      sala 803 Jd. Acácias - Ribeirão Preto - SP
    </address>

    <ul class="contacts">
      <li><span class="label">c</span>(16) 8420-5937</li>
      <li><span class="label">p</span>(16) 3745-8081</li>
      <li><span class="label">e</span>drlucianovarela@mailbox.example</li>
    </ul>
  </section>

</main>
</body>
</html>
```